HOME IMPROVEMENT Business Card

I want a very unique business card. nothing typical and boring. Im open to you ideas. Ive seen cards with gold and silver or color foil and spot UV coatings. Im looking for something that looks cool and grabs attention. I like rounded corners but am open to all suggestions. We are a home improvement company and I will have a presentation folder printed and a catalog printed also and want to keep that same theme. I love the colors in our logo but I am open at looking at a 3rd color that would work with my logo. I hope that helps.
Card should include
Address
Phone
Fax
Email
Website
Target Market(s)
Home owners, people looking to remodel their home
Industry/Entity Type
Home Improvement
Contact Information for Business Card
2873 Maple Crest Avenue Unit 410
Des Plaines, Il 60284
Phone
Direct Line
Email
Website
Font styles to use
Other font styles liked:
- IM OPEN MINDED
Requirements
Must have
- High end quality look nothing boring I like rounded corners but am open minded
Nice to have
- WOW. I want something nice and impressive.
Should not have
- ??? Not sure

```html
<!DOCTYPE html>
<html lang="en">
<head>
<meta charset="utf-8">
<title>Hearthline Business Card</title>
<link href="https://fonts.googleapis.com/css2?family=Open+Sans:wght@400;600;700;800&display=swap" rel="stylesheet">
<style>
  :root {
    --backdrop: #6d6e71;
    --green: #0c9a48;
    --navy: #10103f;
    --white: #ffffff;
    --ink: #2a2a35;
    --grey: #5f6066;
  }
  * { margin: 0; padding: 0; box-sizing: border-box; }
  html, body {
    width: 1200px;
    height: 1083px;
    overflow: hidden;
    background: var(--backdrop);
    font-family: "Open Sans", Arial, sans-serif;
  }
  .card {
    position: absolute;
    left: 284px;
    width: 622px;
    height: 352px;
    border-radius: 22px;
    overflow: hidden;
    box-shadow: 4px 6px 12px rgba(0, 0, 0, 0.35);
  }
  .card-front { top: 158px; background: var(--green); }
  .card-back { top: 576px; background: var(--navy); }
  .card-art {
    position: absolute;
    inset: 0;
    width: 100%;
    height: 100%;
  }
  .brand-name {
    position: absolute;
    font-weight: 800;
    letter-spacing: -0.5px;
    line-height: 1;
    white-space: nowrap;
  }
  .card-front .brand-name {
    left: 0;
    right: 0;
    top: 112px;
    text-align: center;
    font-size: 44px;
    color: var(--white);
  }
  .card-back .brand-name {
    left: 48px;
    top: 84px;
    font-size: 34px;
    color: var(--navy);
  }
  .person {
    position: absolute;
    right: 36px;
    top: 96px;
    text-align: right;
  }
  .person-name {
    font-size: 20px;
    font-weight: 600;
    letter-spacing: 1.5px;
    color: var(--ink);
    line-height: 1.2;
  }
  .person-company {
    margin-top: 5px;
    font-size: 13px;
    letter-spacing: 3px;
    color: var(--grey);
  }
  .contact-list {
    position: absolute;
    right: 32px;
    top: 170px;
    list-style: none;
  }
  .contact-item {
    display: flex;
    justify-content: flex-end;
    align-items: center;
    gap: 10px;
    height: 22.5px;
    font-size: 15px;
    color: var(--grey);
  }
  .contact-item.phone { font-size: 13px; }
  .contact-icon { width: 14px; height: 14px; flex: none; }
  .address {
    position: absolute;
    left: 39px;
    top: 283px;
    font-size: 15px;
    line-height: 22px;
    color: var(--green);
  }
</style>
</head>
<body>

<section class="card card-front" aria-label="Card front">
  <svg class="card-art" viewBox="0 0 415 235" preserveAspectRatio="none" aria-hidden="true">
    <path fill="#10103f" d="M0,165 C80,150 160,150 240,158 C320,166 380,172 415,172 L415,180 C330,178 250,168 170,165 C100,163 40,170 0,178 Z"/>
    <path fill="#10103f" d="M0,182 C60,168 140,162 220,170 C300,178 370,188 415,190 L415,235 L0,235 Z"/>
  </svg>
  <div class="brand-name">Hearthline</div>
</section>

<section class="card card-back" aria-label="Card back">
  <svg class="card-art" viewBox="0 0 415 235" preserveAspectRatio="none" aria-hidden="true">
    <path fill="#ffffff" d="M0,41 H39 V35 L76,24 L113,35 V41 H415 V200 L0,200 Z"/>
    <path fill="#10103f" d="M0,165 C50,154 100,150 160,152 C250,156 340,172 415,182 L415,196 C330,186 240,170 160,168 C100,166 50,172 0,180 Z"/>
    <path fill="#0c9a48" d="M175,152 C260,158 340,170 415,176 L415,184 C340,176 260,164 175,152 Z"/>
    <path fill="#10103f" d="M0,186 C70,174 150,172 230,180 C310,188 370,196 415,196 L415,235 L0,235 Z"/>
  </svg>

  <div class="brand-name">Hearthline</div>

  <div class="person">
    <p class="person-name">DANE HOLLOWAY</p>
    <p class="person-company">NORTHGATE BUILD</p>
  </div>

  <ul class="contact-list">
    <li class="contact-item">
      <span>northgatebuild.com.au</span>
      <svg class="contact-icon" viewBox="0 0 14 14" aria-hidden="true">
        <circle cx="7" cy="7" r="6" fill="#0c9a48"/>
        <g fill="none" stroke="#fff" stroke-width="0.9">
          <ellipse cx="7" cy="7" rx="2.6" ry="6"/>
          <line x1="1" y1="7" x2="13" y2="7"/>
          <line x1="2" y1="4" x2="12" y2="4"/>
          <line x1="2" y1="10" x2="12" y2="10"/>
        </g>
      </svg>
    </li>
    <li class="contact-item">
      <span>hello@northgatebuild.com.au</span>
      <svg class="contact-icon" viewBox="0 0 14 14" aria-hidden="true">
        <rect x="1" y="3" width="12" height="8.5" rx="1" fill="#0c9a48"/>
        <path d="M1.5,3.5 L7,8 L12.5,3.5" fill="none" stroke="#fff" stroke-width="1"/>
      </svg>
    </li>
    <li class="contact-item phone">
      <span>1300 555 014 (1300 NGB 014)</span>
      <svg class="contact-icon" viewBox="0 0 14 14" aria-hidden="true">
        <rect x="3.5" y="0.8" width="7" height="12.4" rx="1.3" fill="none" stroke="#0c9a48" stroke-width="1.4"/>
        <circle cx="7" cy="11" r="0.8" fill="#0c9a48"/>
      </svg>
    </li>
  </ul>

  <address class="address" style="font-style: normal;">
    2873 Maple Crest Avenue Unit 410<br>
    Des Plaines, Il 60284
  </address>
</section>

</body>
</html>
```